Halvorsen Construction Needs a Business Card

Our current business card is very bland, and since we have a new logo, we would like a new business card design to reflect our company. It can be a single-sided or two-sided card, but it is important that our contact information appears on the same side. I am attaching a copy of our old card and our new logo. If you need the logo in another format than the one I'm sending, please let me know. This is the information that we must have on our card, but not necessarily in any specific order:
1) Our logo
2) General Contractor
3) Dale Halvorsen, Owner
4) 482 Commerce Ridge Road, Brookhaven, Ohio 35871
5) Office: 319-555-0147
7) Fax: 319-555-0148
8) Cell: 319-555-0193
9) halvorsenconstruction@qvl-mail.net
10) halvorsenconstruction-example.com (can be omitted if necessary)
Also, I will need files in a format that I can alter if any of the above information changes in the near future. Thank you in advance for your submissions!
Target Market(s)
Commercial and residential clients, architects, and subcontractors.
Industry/Entity Type
Business
Look and feel

```html
<!DOCTYPE html>
<html lang="en">
<head>
<meta charset="utf-8">
<title>Halvorsen Construction – Business Card</title>
<link rel="stylesheet" href="https://fonts.googleapis.com/css2?family=Michroma&family=Play:wght@400&family=Arimo:wght@400&family=Open+Sans:wght@700&display=swap">
<style>
  :root {
    --page-bg: #e6e2dc;
    --card-white: #ffffff;
    --card-black: #0c0c0c;
    --ink: #1c1c1c;
    --accent-yellow: #e4e619;
    --strip-top: #2b2b2b;
    --strip-bottom: #151515;
    --text-light: #ffffff;
  }
  html, body {
    margin: 0;
    width: 1200px;
    height: 1200px;
    overflow: hidden;
    background: var(--page-bg);
  }
  .business-card {
    position: absolute;
    left: 96px;
    top: 316px;
    width: 1010px;
    height: 592px;
    background: linear-gradient(to bottom, var(--card-white) 0, var(--card-white) 150px, var(--card-black) 270px);
    overflow: hidden;
    box-shadow: 0 4px 14px rgba(0,0,0,0.25);
  }
  .skyline-band {
    position: absolute;
    left: 0;
    top: 110px;
    width: 100%;
    height: 180px;
    background: linear-gradient(to bottom, rgba(228,230,25,0) 0%, rgba(228,230,25,0.85) 30%, var(--accent-yellow) 45%, #3a3a0a 65%, var(--card-black) 85%);
  }
  .brand {
    position: absolute;
    left: 234px;
    top: 46px;
    display: flex;
    align-items: center;
    gap: 16px;
  }
  .brand-square {
    width: 116px;
    height: 116px;
    background: var(--ink);
  }
  .brand-name {
    font-family: "Michroma", sans-serif;
    color: var(--ink);
    line-height: 1;
  }
  .brand-name .line-main {
    display: block;
    font-size: 48px;
  }
  .brand-name .line-sub {
    display: block;
    font-size: 22px;
    letter-spacing: 9.5px;
    margin-top: 8px;
  }
  .owner-name {
    position: absolute;
    left: 42px;
    top: 272px;
    margin: 0;
    font-family: "Michroma", sans-serif;
    font-weight: 400;
    font-size: 28px;
    line-height: 36px;
    letter-spacing: 3px;
    color: var(--text-light);
  }
  .owner-title {
    position: absolute;
    left: 42px;
    top: 314px;
    margin: 0;
    font-family: "Play", sans-serif;
    font-size: 24px;
    line-height: 32px;
    color: var(--accent-yellow);
  }
  .contact-list {
    position: absolute;
    left: 42px;
    top: 355px;
    margin: 0;
    padding: 0;
    list-style: none;
    font-family: "Arimo", sans-serif;
    font-size: 25px;
    line-height: 38.5px;
    color: var(--text-light);
  }
  .web-strip {
    position: absolute;
    left: 0;
    bottom: 0;
    width: 100%;
    height: 80px;
    background: linear-gradient(to bottom, var(--strip-top), var(--strip-bottom));
    display: flex;
    justify-content: space-between;
    align-items: center;
    padding: 0 38px 0 42px;
    box-sizing: border-box;
    font-family: "Open Sans", sans-serif;
    font-weight: 700;
    font-size: 17px;
    color: var(--text-light);
  }
</style>
</head>
<body>
  <div class="business-card">
    <div class="skyline-band" role="img" aria-label="City skyline silhouette against a yellow glow"></div>

    <div class="brand">
      <div class="brand-square"></div>
      <div class="brand-name">
        <span class="line-main">HALVORSEN</span>
        <span class="line-sub">CONSTRUCTION</span>
      </div>
    </div>

    <h1 class="owner-name">DALE HALVORSEN</h1>
    <p class="owner-title">General Contractor and Owner</p>

    <ul class="contact-list">
      <li>482 Commerce Ridge Road, Brookhaven, Ohio 35871</li>
      <li>Office: 319-555-0147</li>
      <li>Fax: 319-555-0148</li>
      <li>Cell: 319-555-0193</li>
    </ul>

    <div class="web-strip">
      <span class="email">HALVORSENCONSTRUCTION@QVL-MAIL.NET</span>
      <span class="website">WWW.HALVORSENCONSTRUCTION-EXAMPLE.COM</span>
    </div>
  </div>
</body>
</html>
```